Infografik für Tanzschule
Zielgruppe
Wir sind eine Tanzschule für die Tänze Salsa, Bachata, kizomba & Zouk in Freiburg
Aufgabenstellung
DESIGN-BRIEFING
Tarifübersicht – Tanzschule Ritmo del Alba
Projektziel
Gestaltung einer klaren, hochwertigen Tarifübersicht für eine Tanzschule.
Die Grafik dient: als Information & Orientierung auf der Homepage, als visuelle Grundlage für das Anmeldeformular vor Ort, Der Einstieg erfolgt immer über eine gratis Schnupperstunde.
Die verbindliche Anmeldung erfolgt nach der Schnupperstunde vor Ort über ein Formular mit Auswahlkästchen.
Grundaufbau
3 Tarifkarten nebeneinander
Einheitlicher, moderner Stil
evtl. Emotionale Bilder (echte Tanzszenen, echte Menschen)
Klare Hierarchie:
Titel → Preis → Erklärung → Vorteile → Auswahlkästchen
Struktur der Tarifkarten
KARTE 1 – EINSTIEG
Titel: 1× PRO WOCHE TANZEN
Preis: 56 €/ 39 € erm.
Subline: pro Person · pro Kalendermonat
Vorteile (max. 4 Bulletpoints):
Ein fester wöchentlicher Kurs
Klare Routine & Struktur
Ausweichstunde im selben Monat möglich (muss klar enthalten sein)
Auswahl: ☐ 1× pro Woche tanzen
KARTE 2 – REGELMÄSSIG TANZEN (darf visuell leicht hervorgehoben sein, z. B. Rahmen oder Badge)
Optionales Badge:
SEHR BELIEBT
Titel: 2× PRO WOCHE TANZEN
Preis: 98 € / 68 € erm.
Vorteile:
Zwei feste wöchentliche Kurse
Mehr Praxis & schnellerer Fortschritt
Ausweichstunde im selben Monat möglich
Auswahl:
☐ 2× pro Woche tanzen
KARTE 3 – MAXIMALE FREIHEIT
Titel: FLAT – ALL YOU CAN DANCE
Preis: ab 129 € / 99 € erm.
Alle Tänze
Alle Kurse (für dein Tanz-Level)
Alle Workshops (für dein Tanz-Level)
Maximale Freiheit
☐ FLAT 1 Monat – 149 € | 119 € erm. (monatlich kündbar)
☐ FLAT 3 Monate – 129 € | 99 € erm. (3 Monate Erstlaufzeit)
Einheitlicher Hinweis unter den Karten (kleiner Text)
Ausweic..

```html
<!DOCTYPE html>
<html lang="de">
<head>
<meta charset="utf-8">
<title>Tarifübersicht – Tanzschule Ritmo del Alba</title>
<link href="https://fonts.googleapis.com/css2?family=Nunito:wght@400;500;600;700;800&family=Open+Sans:wght@400;600;700&display=swap" rel="stylesheet">
<style>
:root{
  --accent:#bd1650;
  --accent-soft:#f9d9e3;
  --ink:#1d1b1a;
  --muted:#8b8580;
  --sand:#f2ebe5;
  --card-top:#f8f5f1;
  --card-body:#ffffff;
  --line:#ece4da;
}
*{box-sizing:border-box;margin:0;padding:0}
html,body{width:1200px;height:675px;overflow:hidden;background:#fff}
body{font-family:"Nunito",sans-serif;color:var(--ink);position:relative}

.overview{position:absolute;left:0;top:0;width:725px;height:675px;background:var(--sand)}
.tariffs{position:absolute;left:58px;top:125px;display:flex;gap:7px}
.card{width:198px;height:354px;border-radius:14px;background:var(--card-body);overflow:hidden;display:flex;flex-direction:column}
.card__head{background:var(--card-top);height:130px;padding:22px 12px 0 12px}
.card__title{color:var(--accent);font-weight:700;font-size:17px;line-height:1;white-space:nowrap}
.card__sub{font-size:11px;margin-top:12px;white-space:nowrap}
.card__price{margin-top:11px;display:flex;align-items:baseline;gap:7px;white-space:nowrap}
.card__amount{font-size:25px;font-weight:800;letter-spacing:-.2px}
.card__unit{font-size:11px}
.card__reduced{font-size:8.5px;color:var(--muted);margin-top:7px;white-space:nowrap}
.card__body{padding:20px 12px 0 12px;flex:1;display:flex;flex-direction:column}
.features{list-style:none;height:92px;border-bottom:1px solid var(--line)}
.features li{display:flex;gap:12px;font-size:11px;line-height:13px;margin-bottom:7px}
.tick{flex:none;width:11px;height:11px;margin-top:1px}
.options{padding-top:17px}
.option{display:flex;gap:12px;font-size:11px;line-height:13px;margin-bottom:11px}
.box{flex:none;width:12px;height:12px;border:1.2px solid #2a2826}

.notes{position:absolute;left:58px;top:494px;width:610px;font-size:8.5px;line-height:12px;color:#6e6964}
.notes .terms{margin-top:12px}

/* Anmeldeformular */
.form{position:absolute;left:777px;top:74px;width:372px;height:526px;background:var(--sand);border:1px solid #d9d4cf;font-family:"Open Sans",sans-serif;overflow:hidden}
.form__top{position:absolute;left:0;top:0;width:100%;height:189px;background:#fff}
.form__title{position:absolute;left:27px;top:28px;font-family:"Nunito",sans-serif;font-weight:700;font-size:12.5px;color:var(--accent)}
.brand{position:absolute;left:268px;top:24px;display:flex;align-items:center;gap:4px;font-family:"Nunito",sans-serif;font-weight:700;font-size:9px;color:var(--accent)}
.brand__dot{width:7px;height:7px;border-radius:50%;background:var(--accent)}
.salutation{position:absolute;left:27px;top:57px;display:flex;gap:9px;font-size:5.5px}
.salutation span{display:flex;align-items:center;gap:4px}
.mbox{width:6px;height:6px;border:.7px solid #444;display:inline-block;flex:none}
.field{position:absolute;left:27px;width:211px;border-bottom:.7px solid #444;font-size:5.3px;padding-bottom:2px}
.consent{position:absolute;left:27px;font-size:5.3px;display:flex;align-items:center;gap:5px}
.school{position:absolute;left:268px;top:58px;font-size:5.2px;line-height:7.5px}
.school b{font-weight:700}
.school p{margin-bottom:7px}

/* kleine Tarifkarten im Formular */
.tariffs.mini{left:27px;top:203px;gap:4px}
.mini .card{width:104px;height:167px;border-radius:7px}
.mini .card__head{height:58px;padding:7px 6px 0 6px}
.mini .card__title{font-size:9px}
.mini .card__sub{font-size:5.3px;margin-top:7px}
.mini .card__price{margin-top:5px;gap:4px}
.mini .card__amount{font-size:12px;letter-spacing:0}
.mini .card__unit{font-size:5.2px}
.mini .card__reduced{font-size:4px;margin-top:3px}
.mini .card__body{padding:7px 6px 0 6px}
.mini .features{height:42px;border-bottom-width:.6px}
.mini .features li{font-size:5.3px;line-height:6.6px;gap:6px;margin-bottom:3.5px}
.mini .tick{width:5.5px;height:5.5px;margin-top:.5px}
.mini .options{padding-top:9px}
.mini .option{font-size:5.3px;line-height:6.6px;gap:6px;margin-bottom:4.5px}
.mini .box{width:6px;height:6px;border-width:.7px}

.panel{position:absolute;background:#fff;border-radius:7px}
.sepa{left:27px;top:375px;width:318px;height:68px;padding:6px 6px}
.panel__label{font-size:5.6px;font-weight:600}
.sepa__text{font-size:3.9px;line-height:5.4px;color:#6d6863;margin-top:1px}
.sepa .field{position:relative;left:0;width:100%;margin-top:9px}
.sepa .field + .field{margin-top:8px}
.start{left:27px;top:447px;width:157px;height:36px;padding:6px 6px}
.months{display:flex;justify-content:space-between;margin-top:5px;padding:0 2px}
.months span{display:flex;flex-direction:column;align-items:center;gap:2px;font-size:3.9px}
.sign{left:190px;top:447px;width:155px;height:36px;padding:6px 6px}
.sign small{display:block;font-size:3.9px;color:#6d6863;margin-top:1px}
.sign .rule{border-bottom:.7px solid #444;margin-top:12px}
.form__foot{position:absolute;left:27px;top:491px;width:318px;font-size:3.9px;line-height:6px;color:#6d6863}
</style>
</head>
<body>

<section class="overview">
  <div class="tariffs">
    <article class="card">
      <header class="card__head">
        <h2 class="card__title">Einstieg</h2>
        <p class="card__sub">1× pro Woche tanzen</p>
        <p class="card__price"><span class="card__amount">€ 56,-</span><span class="card__unit">pro Person/Monat</span></p>
        <p class="card__reduced">€ 39,- erm.* pro Person/Monat</p>
      </header>
      <div class="card__body">
        <ul class="features">
          <li><svg class="tick" viewBox="0 0 12 12"><circle cx="6" cy="6" r="6" fill="#f9d9e3"/><path d="M3.3 6.1l1.9 1.8 3.6-3.7" fill="none" stroke="#bd1650" stroke-width="1.3"/></svg>Ein fester wöchentlicher Kurs</li>
          <li><svg class="tick" viewBox="0 0 12 12"><circle cx="6" cy="6" r="6" fill="#f9d9e3"/><path d="M3.3 6.1l1.9 1.8 3.6-3.7" fill="none" stroke="#bd1650" stroke-width="1.3"/></svg>Klare Routine &amp; Struktur</li>
          <li><svg class="tick" viewBox="0 0 12 12"><circle cx="6" cy="6" r="6" fill="#f9d9e3"/><path d="M3.3 6.1l1.9 1.8 3.6-3.7" fill="none" stroke="#bd1650" stroke-width="1.3"/></svg><span>Ausweichstunde** im<br>selben Monat möglich</span></li>
        </ul>
        <div class="options">
          <div class="option"><span class="box"></span>1× pro Woche tanzen</div>
        </div>
      </div>
    </article>

    <article class="card">
      <header class="card__head">
        <h2 class="card__title">Regelmäßig tanzen</h2>
        <p class="card__sub">2× pro Woche tanzen</p>
        <p class="card__price"><span class="card__amount">€ 98,-</span><span class="card__unit">pro Person/Monat</span></p>
        <p class="card__reduced">€ 68,- erm.* pro Person/Monat</p>
      </header>
      <div class="card__body">
        <ul class="features">
          <li><svg class="tick" viewBox="0 0 12 12"><circle cx="6" cy="6" r="6" fill="#f9d9e3"/><path d="M3.3 6.1l1.9 1.8 3.6-3.7" fill="none" stroke="#bd1650" stroke-width="1.3"/></svg>Zwei feste wöchentliche Kurse</li>
          <li><svg class="tick" viewBox="0 0 12 12"><circle cx="6" cy="6" r="6" fill="#f9d9e3"/><path d="M3.3 6.1l1.9 1.8 3.6-3.7" fill="none" stroke="#bd1650" stroke-width="1.3"/></svg><span>Mehr Praxis &amp;<br>schnellerer Fortschritt</span></li>
          <li><svg class="tick" viewBox="0 0 12 12"><circle cx="6" cy="6" r="6" fill="#f9d9e3"/><path d="M3.3 6.1l1.9 1.8 3.6-3.7" fill="none" stroke="#bd1650" stroke-width="1.3"/></svg><span>Ausweichstunde** im<br>selben Monat möglich</span></li>
        </ul>
        <div class="options">
          <div class="option"><span class="box"></span>2× pro Woche tanzen</div>
        </div>
      </div>
    </article>

    <article class="card">
      <header class="card__head">
        <h2 class="card__title">Maximale Freiheit</h2>
        <p class="card__sub">Flat – All you can dance.</p>
        <p class="card__price"><span class="card__amount">€ 129,-</span><span class="card__unit">pro Person/Monat</span></p>
        <p class="card__reduced">€ 99,- erm.* pro Person/Monat</p>
      </header>
      <div class="card__body">
        <ul class="features">
          <li><svg class="tick" viewBox="0 0 12 12"><circle cx="6" cy="6" r="6" fill="#f9d9e3"/><path d="M3.3 6.1l1.9 1.8 3.6-3.7" fill="none" stroke="#bd1650" stroke-width="1.3"/></svg>Alle Tänze</li>
          <li><svg class="tick" viewBox="0 0 12 12"><circle cx="6" cy="6" r="6" fill="#f9d9e3"/><path d="M3.3 6.1l1.9 1.8 3.6-3.7" fill="none" stroke="#bd1650" stroke-width="1.3"/></svg><span>Alle Kurse<br>(für dein Tanz-Level)</span></li>
          <li><svg class="tick" viewBox="0 0 12 12"><circle cx="6" cy="6" r="6" fill="#f9d9e3"/><path d="M3.3 6.1l1.9 1.8 3.6-3.7" fill="none" stroke="#bd1650" stroke-width="1.3"/></svg><span>Alle Workshops<br>(für dein Tanz-Level)</span></li>
        </ul>
        <div class="options">
          <div class="option"><span class="box"></span><span>FLAT 1 Monat<br>€ 149,- | € 119,- erm.<br>(monatlich kündbar)</span></div>
          <div class="option"><span class="box"></span><span>FLAT 3 Monate<br>€ 129,- | € 99,- erm.<br>(3 Monate Erstlaufzeit)</span></div>
        </div>
      </div>
    </article>
  </div>

  <div class="notes">
    <p>* Für Studierende, Schüler*Innen und Auszubildende haben wir ermäßigte Tarife.</p>
    <p>**Ausweichstunde: Im selben Kalendermonat möglich.</p>
    <p class="terms">Verlängerung &amp; Kündigung: Der Vertrag verlängert sich automatisch um jeweils einen Monat und ist mit 14 Tagen Frist zum Monatsende kündbar. Ausnahme: FLAT 3 Monate – kündbar nach Ablauf der Erstlaufzeit.</p>
  </div>
</section>

<section class="form">
  <div class="form__top"></div>
  <h1 class="form__title">Anmeldeformular</h1>
  <div class="brand"><span class="brand__dot"></span>Ritmo del Alba</div>

  <div class="salutation">
    <span><i class="mbox"></i>Frau</span><span><i class="mbox"></i>Herr</span><span><i class="mbox"></i>Div.</span>
  </div>
  <div class="field" style="top:73px">Vor- &amp; Nachname:</div>
  <div class="field" style="top:90px">Staße, Nr.:</div>
  <div class="field" style="top:107px">Plz, Ort:</div>
  <div class="field" style="top:125px">Telefon:</div>
  <div class="field" style="top:142px">E-Mail:</div>
  <div class="consent" style="top:158px"><i class="mbox"></i>Ermäßigt (Student*in / Schüler*in / Auszubildende*r)</div>
  <div class="consent" style="top:170px"><i class="mbox"></i>Ja, ich möchte den Newsletter und Kursinformationen erhalten.</div>

  <div class="school">
    <p><b>Tanzschule Ritmo del Alba</b><br>Lindenweg 14<br>79100 Freiburg im Breisgau</p>
    <p><b>Geschäftsanschrift</b><br>Martin Keller<br>Ahornstraße 8<br>79102 Freiburg im Breisgau</p>
    <p><b>Kontakt</b><br>0151 44 218 907<br>kontakt@ritmo-del-alba.de<br>ritmo-del-alba.de</p>
  </div>

  <div class="tariffs mini">
    <article class="card">
      <header class="card__head">
        <h2 class="card__title">Einstieg</h2>
        <p class="card__sub">1× pro Woche tanzen</p>
        <p class="card__price"><span class="card__amount">€ 56,-</span><span class="card__unit">pro Person/Monat</span></p>
        <p class="card__reduced">€ 39,- ermäßigt pro Person/Monat</p>
      </header>
      <div class="card__body">
        <ul class="features">
          <li><svg class="tick" viewBox="0 0 12 12"><circle cx="6" cy="6" r="6" fill="#f9d9e3"/><path d="M3.3 6.1l1.9 1.8 3.6-3.7" fill="none" stroke="#bd1650" stroke-width="1.3"/></svg>Ein fester wöchentlicher Kurs</li>
          <li><svg class="tick" viewBox="0 0 12 12"><circle cx="6" cy="6" r="6" fill="#f9d9e3"/><path d="M3.3 6.1l1.9 1.8 3.6-3.7" fill="none" stroke="#bd1650" stroke-width="1.3"/></svg>Klare Routine &amp; Struktur</li>
          <li><svg class="tick" viewBox="0 0 12 12"><circle cx="6" cy="6" r="6" fill="#f9d9e3"/><path d="M3.3 6.1l1.9 1.8 3.6-3.7" fill="none" stroke="#bd1650" stroke-width="1.3"/></svg><span>Ausweichstunde* im<br>selben Monat möglich</span></li>
        </ul>
        <div class="options"><div class="option"><span class="box"></span>1× pro Woche tanzen</div></div>
      </div>
    </article>
    <article class="card">
      <header class="card__head">
        <h2 class="card__title">Regelmäßig tanzen</h2>
        <p class="card__sub">2× pro Woche tanzen</p>
        <p class="card__price"><span class="card__amount">€ 98,-</span><span class="card__unit">pro Person/Monat</span></p>
        <p class="card__reduced">€ 68,- ermäßigt pro Person/Monat</p>
      </header>
      <div class="card__body">
        <ul class="features">
          <li><svg class="tick" viewBox="0 0 12 12"><circle cx="6" cy="6" r="6" fill="#f9d9e3"/><path d="M3.3 6.1l1.9 1.8 3.6-3.7" fill="none" stroke="#bd1650" stroke-width="1.3"/></svg>Zwei feste wöchentliche Kurse</li>
          <li><svg class="tick" viewBox="0 0 12 12"><circle cx="6" cy="6" r="6" fill="#f9d9e3"/><path d="M3.3 6.1l1.9 1.8 3.6-3.7" fill="none" stroke="#bd1650" stroke-width="1.3"/></svg><span>Mehr Praxis &amp;<br>schnellerer Fortschritt</span></li>
          <li><svg class="tick" viewBox="0 0 12 12"><circle cx="6" cy="6" r="6" fill="#f9d9e3"/><path d="M3.3 6.1l1.9 1.8 3.6-3.7" fill="none" stroke="#bd1650" stroke-width="1.3"/></svg><span>Ausweichstunde* im<br>selben Monat möglich</span></li>
        </ul>
        <div class="options"><div class="option"><span class="box"></span>2× pro Woche tanzen</div></div>
      </div>
    </article>
    <article class="card">
      <header class="card__head">
        <h2 class="card__title">Maximale Freiheit</h2>
        <p class="card__sub">Flat – All you can dance.</p>
        <p class="card__price"><span class="card__amount">€ 129,-</span><span class="card__unit">pro Person/Monat</span></p>
        <p class="card__reduced">€ 99,- ermäßigt pro Person/Monat</p>
      </header>
      <div class="card__body">
        <ul class="features">
          <li><svg class="tick" viewBox="0 0 12 12"><circle cx="6" cy="6" r="6" fill="#f9d9e3"/><path d="M3.3 6.1l1.9 1.8 3.6-3.7" fill="none" stroke="#bd1650" stroke-width="1.3"/></svg>Alle Tänze</li>
          <li><svg class="tick" viewBox="0 0 12 12"><circle cx="6" cy="6" r="6" fill="#f9d9e3"/><path d="M3.3 6.1l1.9 1.8 3.6-3.7" fill="none" stroke="#bd1650" stroke-width="1.3"/></svg><span>Alle Kurse<br>(für dein Tanz-Level)</span></li>
          <li><svg class="tick" viewBox="0 0 12 12"><circle cx="6" cy="6" r="6" fill="#f9d9e3"/><path d="M3.3 6.1l1.9 1.8 3.6-3.7" fill="none" stroke="#bd1650" stroke-width="1.3"/></svg><span>Alle Workshops<br>(für dein Tanz-Level)</span></li>
        </ul>
        <div class="options">
          <div class="option"><span class="box"></span><span>FLAT 1 Monat<br>€ 149,- | € 119,- erm.<br>(monatlich kündbar)</span></div>
          <div class="option"><span class="box"></span><span>FLAT 3 Monate<br>€ 129,- | € 99,- erm.<br>(3 Monate Erstlaufzeit)</span></div>
        </div>
      </div>
    </article>
  </div>

  <div class="panel sepa">
    <p class="panel__label">Einzugsermächtigung / SEPA-Lastschriftmandat</p>
    <p class="sepa__text">Ich ermächtige Ritmo del Alba, Zahlungen von meinem Konto per Lastschrift einzuziehen. Zugleich weise ich mein Kreditinstitut an, diese Lastschriften einzulösen. Bei Rückbuchung fallen Gebühren an. Innerhalb von acht Wochen kann ich die Erstattung verlangen. Die Kursgebühr wird jeweils zum 05. des Monats eingezogen.</p>
    <div class="field">Kreditinsitut:</div>
    <div class="field">IBAN:</div>
  </div>

  <div class="panel start">
    <p class="panel__label">Kursstart / Anmeldung ab:</p>
    <div class="months">
      <span>Jan<i class="mbox"></i></span><span>Feb<i class="mbox"></i></span><span>Mrz<i class="mbox"></i></span><span>Apr<i class="mbox"></i></span><span>Mai<i class="mbox"></i></span><span>Jun<i class="mbox"></i></span><span>Jul<i class="mbox"></i></span><span>Aug<i class="mbox"></i></span><span>Sep<i class="mbox"></i></span><span>Okt<i class="mbox"></i></span><span>Nov<i class="mbox"></i></span><span>Dez<i class="mbox"></i></span>
    </div>
  </div>

  <div class="panel sign">
    <p class="panel__label">Datum / Unterschrift:</p>
    <small>Wir verweisen auf unsere umseitig abgedruckten AGB</small>
    <div class="rule"></div>
  </div>

  <div class="form__foot">
    Verlängerung &amp; Kündigung: Der Vertrag verlängert sich automatisch um jeweils einen Monat und ist mit 14 Tagen Frist zum Monatsende kündbar.<br>
    Ausnahme „FLAT 3 Monate“ kündbar nach Ablauf der Erstlaufzeit.<br>
    *Ausweichstunde: Im selben Kalendermonat möglich.
  </div>
</section>

</body>
</html>
```